K Velmor Architectural Construction & Abatement, Inc.
K Velmor Architectural Construction, Inc.
Pilo 47:
86# Has very little orange. Use these colors please. Read all the reviews I gave other designers. Incorporate these ideas into to your design. Push forth these ideas.
Thank you,
rovatique:
Use more green color. Green on back of the card. And on stationary. Continue to push forth with these ideas.
Trulsen:
# 83 Remove the fax information on stationary
# 83 remove the black color on cards & Stationary. Use the original colors. Place motto on back as well.
Use little more green color on front. Green Energy feel. Use the orange as well. Put the logos on envelopes.
erovatique:
Please, include my education on the business cards. BArch, MArch. Thank You.
Pilo47:
Please, find away to include my education details on my business cards: BArch, MArch
I like some of the cards you have put together so far. And I have selected my favorites my star rating system. I asked that the front remain the same. But, the back have another logo which says K Velmor Architect ABATEMENT. I will upload the design for the business cards. Continue, to push the ideas.

```html
<!DOCTYPE html>
<html lang="en">
<head>
<meta charset="utf-8">
<title>Velmor Architects – Business Card</title>
<link rel="stylesheet" href="https://fonts.googleapis.com/css2?family=Source+Sans+3:wght@400;600;700&display=swap">
<style>
  :root {
    --backdrop: #e9e6e1;
    --card-white: #ffffff;
    --brand-orange: #f26a0f;
    --brand-orange-deep: #e55d05;
    --brand-green: #5cb531;
    --brand-green-soft: #eef7e8;
    --brand-slate: #1f3a5a;
    --text-light: #ffffff;
    --text-soft: #fff2e6;
  }
  * { box-sizing: border-box; margin: 0; padding: 0; }
  html, body {
    width: 1200px; height: 780px; overflow: hidden;
    background: var(--backdrop);
    font-family: "Source Sans 3", "Myriad Pro", Arial, sans-serif;
  }
  .business-card {
    position: absolute; left: 100px; top: 105px;
    width: 1000px; height: 570px;
    border-radius: 34px; overflow: hidden;
    background: linear-gradient(180deg, var(--card-white) 55%, var(--brand-green-soft) 100%);
    box-shadow: 0 10px 30px rgba(0,0,0,0.22);
  }
  .brand-lockup {
    position: absolute; left: 0; right: 0; top: 120px;
    display: flex; align-items: center; justify-content: center; gap: 22px;
  }
  .brand-mark {
    width: 72px; height: 72px; border-radius: 8px;
    background: var(--brand-green);
  }
  .brand-name {
    font-size: 64px; font-weight: 700; letter-spacing: 1px;
    color: var(--brand-slate); text-transform: uppercase; line-height: 1;
  }
  .brand-motto {
    position: absolute; left: 0; right: 0; top: 224px;
    text-align: center; font-size: 24px; font-weight: 600;
    letter-spacing: 3px; text-transform: uppercase;
    color: var(--brand-green);
  }
  .accent-rule {
    position: absolute; left: 0; right: 0; top: 348px; height: 12px;
    background: var(--brand-green);
  }
  .contact-band {
    position: absolute; left: 0; right: 0; top: 364px; bottom: 0;
    background: linear-gradient(180deg, var(--brand-orange) 0%, var(--brand-orange-deep) 100%);
    color: var(--text-light);
  }
  .person-line {
    position: absolute; left: 140px; top: 34px;
    display: flex; align-items: baseline; gap: 12px; white-space: nowrap;
  }
  .person-name { font-size: 32px; font-weight: 700; }
  .person-degrees { font-size: 22px; font-weight: 600; margin-left: -6px; }
  .person-divider { font-size: 32px; font-weight: 400; }
  .person-title { font-size: 24px; font-weight: 600; }
  .postal-address {
    position: absolute; left: 140px; top: 100px;
    font-size: 24px; line-height: 34px; font-style: normal;
    color: var(--text-soft);
  }
  .column-divider {
    position: absolute; left: 432px; top: 100px;
    width: 2px; height: 68px; background: var(--text-light);
  }
  .contact-list {
    position: absolute; left: 454px; top: 96px;
    list-style: none; font-size: 24px; line-height: 36px;
  }
  .contact-item { display: flex; align-items: center; gap: 12px; }
  .contact-icon { width: 22px; height: 26px; flex: none; }
</style>
</head>
<body>
  <article class="business-card">
    <header class="brand-lockup">
      <span class="brand-mark"></span>
      <span class="brand-name">Velmor Architects</span>
    </header>
    <p class="brand-motto">Building a greener tomorrow</p>
    <div class="accent-rule"></div>
    <section class="contact-band">
      <div class="person-line">
        <span class="person-name">Marlon Teague</span>
        <span class="person-degrees">, BArch, MArch</span>
        <span class="person-divider">/</span>
        <span class="person-title">Architect Intern / Project Manager</span>
      </div>
      <address class="postal-address">
        5320 County Road 208<br>
        Brenham, Texas 77833
      </address>
      <div class="column-divider"></div>
      <ul class="contact-list">
        <li class="contact-item">
          <svg class="contact-icon" viewBox="0 0 22 26" aria-hidden="true">
            <rect x="5" y="2" width="12" height="22" rx="2.5" fill="none" stroke="#fff" stroke-width="2"/>
            <rect x="8" y="6" width="6" height="8" fill="#fff"/>
            <circle cx="11" cy="19.5" r="1.6" fill="#fff"/>
          </svg>
          <span>(555) 318-2074</span>
        </li>
        <li class="contact-item">
          <svg class="contact-icon" viewBox="0 0 22 26" aria-hidden="true">
            <text x="11" y="20" text-anchor="middle" font-size="22" font-weight="700" fill="#fff" font-family="Source Sans 3, sans-serif">@</text>
          </svg>
          <span>kvelmorbuild@postmail.com</span>
        </li>
      </ul>
    </section>
  </article>
</body>
</html>
```